4 Poster Designs required for Nail Salon

We require 4 poster designs that will be displayed inside a shopping centre. Each design should contain our logo and the words "Located next to TallMart" (or similar). Design 1 (MOTHERS DAY) should contain the words "Mothers Day Special" and "$10 gift voucher when you spend over $50". Design 2 (CHRISTMAS) should contain the words "Christmas in July" and "Purchase a set of nails and get a $10 gift voucher". Design 3 (ALL YEAR) should contain the words "New Deluxe Spa Pedicure Service" and the words "Try our new Deluxe Spa Pedicure and get a free nail buff, shape and polish for your fingernails". Design 4 (ALL YEAR 2)should contain high quality nail salon image(s) and the words "Now Open". We like designs that support our image of high quality/fun/clean and safe.
Updates
I will close this early. In 24 hours.
Target Market(s)
Rich mums
Industry/Entity Type
Shopping
Look and feel
Each slider illustrates characteristics of the customer's brand and the style your logo design should communicate.

```html
<!DOCTYPE html>
<html lang="en">
<head>
<meta charset="utf-8">
<title>Lumen Nail Salon – Mothers Day Special Offer</title>
<link href="https://fonts.googleapis.com/css2?family=Nunito:wght@800;900&family=Open+Sans:ital,wght@0,400;0,600;0,700;1,700&family=Alegreya:wght@800&display=swap" rel="stylesheet">
<style>
  :root {
    --pink: #e4398f;
    --pink-deep: #d0287f;
    --magenta: #c02b8e;
    --purple: #8a2b98;
    --violet: #6a3aa4;
    --blue: #3aa6e2;
    --blue-light: #6fcdf2;
    --cream: #efe8d6;
    --white: #ffffff;
    --ink: #111111;
    --logo-pink: #d8569d;
  }
  * { margin: 0; padding: 0; box-sizing: border-box; }
  html, body { width: 848px; height: 1200px; overflow: hidden; background: #fff; }
  .poster {
    position: relative;
    width: 848px;
    height: 1200px;
    overflow: hidden;
    background: linear-gradient(90deg, var(--pink) 0%, #d44a9e 35%, #9a5fb8 65%, var(--blue) 100%);
    font-family: "Open Sans", Arial, sans-serif;
  }
  .hero-photo {
    position: absolute;
    left: 0; top: 0;
    width: 848px; height: 640px;
    background:
      radial-gradient(ellipse 220px 200px at 360px 170px, #e9b59c 0%, rgba(233,181,156,0) 100%),
      radial-gradient(ellipse 200px 180px at 700px 260px, #d94f9d 0%, rgba(217,79,157,0) 100%),
      radial-gradient(ellipse 260px 220px at 560px 420px, #e8ecc4 0%, rgba(232,236,196,0) 100%),
      radial-gradient(ellipse 220px 200px at 220px 430px, #d9a373 0%, rgba(217,163,115,0) 100%),
      linear-gradient(180deg, #6b6a3e 0%, #8a7c4a 40%, #b68c6a 100%);
    -webkit-mask-image: linear-gradient(180deg, #000 70%, transparent 100%);
    mask-image: linear-gradient(180deg, #000 70%, transparent 100%);
  }
  .brand {
    position: absolute;
    left: 548px; top: 28px;
    width: 274px; height: 120px;
    background: var(--logo-pink);
    color: var(--white);
    text-align: right;
    padding: 28px 38px 0 0;
  }
  .brand-name { font-size: 42px; font-weight: 400; letter-spacing: 3px; line-height: 1; }
  .brand-tag { font-size: 13px; font-weight: 400; margin-top: 6px; }
  .headline {
    position: absolute;
    left: 0; top: 540px; width: 848px;
    text-align: center;
    font-family: "Nunito", Arial, sans-serif;
    font-weight: 900;
    color: var(--pink-deep);
    text-shadow: 3px 0 #fff, -3px 0 #fff, 0 3px #fff, 0 -3px #fff, 2px 2px #fff, -2px -2px #fff, 2px -2px #fff, -2px 2px #fff;
  }
  .headline-main { font-size: 70px; line-height: 80px; }
  .headline-sub { font-size: 48px; line-height: 56px; }
  .offer-band {
    position: absolute;
    left: 0; top: 800px;
    width: 848px; height: 152px;
    background: linear-gradient(180deg, var(--blue-light) 0%, var(--blue) 100%);
  }
  .offer-text {
    position: absolute;
    left: 270px; top: 800px; width: 540px;
    text-align: center;
    font-style: italic; font-weight: 700;
    font-size: 60px; line-height: 70px;
    color: var(--white);
    padding-top: 2px;
  }
  .offer-text .amount { color: var(--ink); }
  .location-band {
    position: absolute;
    left: 0; top: 952px;
    width: 848px; height: 106px;
    background: linear-gradient(90deg, var(--magenta) 0%, var(--purple) 50%, var(--violet) 100%);
  }
  .location {
    position: absolute;
    left: 0; top: 998px; width: 848px;
    text-align: center;
    font-family: "Alegreya", Georgia, serif;
    font-weight: 800; font-size: 40px; letter-spacing: 6px;
    color: var(--white);
    text-shadow: 2px 2px 2px rgba(0,0,0,0.5);
  }
  .voucher-badge { position: absolute; left: 26px; top: 744px; width: 242px; height: 242px; z-index: 2; }
  .voucher-copy {
    position: absolute;
    left: 26px; top: 790px; width: 242px;
    text-align: center; color: var(--white);
    z-index: 3;
  }
  .voucher-value { font-weight: 700; font-size: 76px; line-height: 84px; }
  .voucher-label { font-weight: 600; font-size: 30px; line-height: 34px; }
  .contact {
    position: absolute;
    left: 0; top: 1058px;
    width: 848px; height: 142px;
    background: var(--cream);
    text-align: center;
    color: var(--pink-deep);
    font-weight: 700;
  }
  .contact-phone { font-size: 35px; line-height: 44px; margin-top: 28px; margin-left: -64px; }
  .contact-email { font-size: 25px; font-weight: 600; line-height: 34px; margin-top: 2px; margin-left: -48px; }
</style>
</head>
<body>
<main class="poster">
  <div class="hero-photo" role="img" aria-label="Photo of a smiling mother hugging her young daughter, holding a bouquet of pink daisies"></div>

  <div class="brand">
    <div class="brand-name">Lumen</div>
    <div class="brand-tag">Nail Salon</div>
  </div>

  <h1 class="headline">
    <div class="headline-main">Mothers Day</div>
    <div class="headline-sub">Special offer</div>
  </h1>

  <div class="offer-band"></div>
  <p class="offer-text">when you spend<br>over <span class="amount">$50</span></p>

  <div class="location-band"></div>
  <p class="location">Located next to TallMart</p>

  <svg class="voucher-badge" viewBox="0 0 242 242" aria-hidden="true">
    <circle cx="121" cy="121" r="120" fill="#ffffff"/>
    <circle cx="121" cy="121" r="110" fill="#8e2d9a" stroke="#8e2d9a" stroke-width="12" stroke-dasharray="7 5"/>
    <circle cx="121" cy="121" r="106" fill="#8e2d9a"/>
  </svg>
  <div class="voucher-copy">
    <div class="voucher-value">$10</div>
    <div class="voucher-label">Gift voucher</div>
  </div>

  <footer class="contact">
    <p class="contact-phone">call us now : 00 0000 00000</p>
    <p class="contact-email">hello@lumennails.com</p>
  </footer>
</main>
</body>
</html>
```